POSTER FOR NEW MUSIC-THEATRE PRODUCTION - De Molenkantelaar

For our new theatre production 'Kraaienwals' we're looking for a new poster design.

All details can be found in the itinerary in attachment.
Updates

Dear designers

Thanks for some really good designs up to now.
Detailed feedback will follow from next week onwards since Im abroad for business and since I have very little internet access.

kind regards
Joris Kint

Target Market(s)

Theatres throughout Flanders (Belgium) when on tour in 2010-2011-2012. (expecting 70 performances)
Age is 14 up till 88 years old.

Requirements
Must have
• see itinerary in attachment
Nice to have
• Take a look to the poster design of our former production. We kind of liked the 'cool' look.
• Mind : use the new logo in attachment
Should not have
• too many colours.

```html
<!DOCTYPE html>
<html lang="nl">
<head>
<meta charset="utf-8">
<title>De Molenkantelaar speelt Kraaienwals</title>
<link rel="stylesheet" href="https://fonts.googleapis.com/css2?family=Orbitron:wght@900&family=Oswald:wght@200;300;400&family=Crimson+Text:wght@700&display=swap">
<style>
  :root {
    --ink: #ffffff;
    --cyan: #2fd3e0;
    --deep: #0a0305;
    --grey: #8c8c8c;
    --logo-red: #e3212a;
  }
  html, body { margin: 0; padding: 0; overflow: hidden; background: var(--deep); }
  .poster {
    position: relative; width: 900px; height: 1200px; overflow: hidden;
    background: var(--deep);
    font-family: "Oswald", "Arial Narrow", sans-serif; font-weight: 300; color: var(--ink);
  }
  .artwork {
    position: absolute; inset: 0;
    background:
      linear-gradient(90deg, transparent 460px, rgba(255,70,90,.55) 463px, rgba(255,120,130,.8) 467px, rgba(255,70,90,.55) 471px, transparent 474px),
      radial-gradient(ellipse 260px 220px at 430px 900px, rgba(226,40,66,.85), transparent 70%),
      radial-gradient(ellipse 300px 260px at 280px 980px, rgba(200,30,55,.6), transparent 70%),
      radial-gradient(ellipse 260px 300px at 700px 560px, rgba(150,40,90,.75), transparent 70%),
      radial-gradient(ellipse 240px 260px at 820px 300px, rgba(140,35,80,.55), transparent 70%),
      radial-gradient(ellipse 280px 320px at 130px 620px, rgba(110,20,30,.6), transparent 70%),
      radial-gradient(ellipse 420px 300px at 450px 380px, rgba(120,22,40,.7), transparent 75%),
      linear-gradient(180deg, #1a0508 0%, #3a0b16 40%, #2a0710 75%, #0a0305 100%);
  }
  .presenter {
    position: absolute; left: 57px; top: 76px; margin: 0;
    font-size: 40px; font-weight: 200; letter-spacing: 1px; line-height: 1;
    transform: scaleX(0.88); transform-origin: left top;
  }
  .title {
    position: absolute; left: 54px; top: 122px; margin: 0; white-space: nowrap;
    transform: scaleX(0.82); transform-origin: left top;
  }
  .title span {
    display: block; font-family: "Orbitron", sans-serif; font-weight: 900;
    font-size: 122px; line-height: 1; letter-spacing: 0; text-transform: uppercase;
  }
  .title .fill { color: var(--ink); position: relative; }
  .title .echo {
    position: absolute; left: 9px; top: 18px; color: transparent;
    -webkit-text-stroke: 2px var(--cyan);
  }
  .credits {
    position: absolute; left: 617px; top: 322px; margin: 0;
    display: grid; grid-template-columns: 148px auto;
    font-size: 14px; line-height: 21.5px; text-transform: uppercase;
  }
  .credits dt { color: var(--cyan); font-weight: 400; grid-column: 1; }
  .credits dd { margin: 0; grid-column: 2; font-weight: 200; }
  .credits .gap { margin-top: 21px; }
  .contact {
    position: absolute; right: 57px; top: 890px; text-align: right;
    font-size: 14px; line-height: 21px; text-transform: uppercase;
  }
  .contact .web { color: var(--cyan); font-weight: 400; }
  .contact .label { font-weight: 400; margin-top: 9px; }
  .producer {
    margin: 6px 0 6px; font-family: "Crimson Text", serif; font-weight: 700;
    font-size: 20px; line-height: 1.1; text-transform: none;
  }
  .contact .details { color: #d8d8d8; font-weight: 200; }
  .sponsors {
    position: absolute; right: 55px; top: 1096px; display: flex; align-items: center; gap: 14px;
  }
  .sponsors .support {
    font-family: "Crimson Text", serif; font-weight: 700; font-size: 15px;
    line-height: 20px; text-align: right;
  }
  .sponsors .badge { width: 46px; height: 46px; background: var(--ink); opacity: .9; }
  .sponsors .badge.red { width: 56px; height: 56px; background: var(--logo-red); opacity: 1; }
  .company {
    position: absolute; left: 40px; top: 1140px; display: flex; align-items: center; gap: 8px;
    font-size: 16px; font-weight: 400; color: var(--grey); text-transform: uppercase; letter-spacing: 1px;
  }
  .company .dot { width: 14px; height: 14px; border-radius: 50%; background: var(--grey); }
</style>
</head>
<body>
<main class="poster">
  <div class="artwork" role="img" aria-label="Abstract digital artwork of streaking red light beams and angular crimson shapes on black"></div>

  <p class="presenter">DE MOLENKANTELAAR SPEELT</p>
  <h1 class="title"><span class="echo" aria-hidden="true">Kraaienwals</span><span class="fill">Kraaienwals</span></h1>

  <dl class="credits">
    <dt>Tekst/regie</dt><dd>Stijn Verhoeve</dd>
    <dt>Spel en muziek</dt><dd>Jelle Maesens</dd>
    <dd>Jonas Dierckx</dd>
    <dd>Floris Maesens</dd>
    <dd>Wim Maesens</dd>
    <dd>Joris Kint</dd>
    <dt class="gap">Techniek</dt><dd class="gap">Lotte Vranckx</dd>
    <dt>Kostuum</dt><dd>Elke Coppens</dd>
  </dl>

  <div class="contact">
    <div class="web">www.molenkantelaar.be</div>
    <div class="label">Boeking/info</div>
    <div class="producer">Lantaarn<br>Produkties</div>
    <div class="details">Lantaarn Produkties<br>03 555 0148<br>info@lantaarn-produkties.be</div>
  </div>

  <div class="sponsors">
    <div class="support">Met steun van de<br>Gewestelijke Kunstraad</div>
    <div class="badge"></div>
    <div class="badge red"></div>
  </div>

  <div class="company"><span class="dot"></span>De Molenkantelaar</div>
</main>
</body>
</html>
```